Casino with the 'highest winning percentage' needs a stationery design

This is for a casino in Colombo, Sri Lanka and we need a stationery design for business card, letter head and envelope.

Should be very professional, simple and elegant without fancy fonts

Reason: Not fully satisfied with the designs. Need more designs.

Industry/Entity Type

Business

Requirements
Must have
• 1. card deck symbol 'CLUBS' in red, or black

2. name in BLOCK CAPITAL LETTERS

3. Preferred font colours are black, white or red

4. Prefer 'professional /elegant' fonts
Should not have
• SHOULD NOT HAVE ANY OTHER SYMBOL EXCEPT 'CLUBS'

DO NOT PREFER ITALIC FONTS

```html
<!DOCTYPE html>
<html lang="en">
<head>
<meta charset="utf-8">
<title>Crestmoor Casino Colombo – Business Card</title>
<link rel="stylesheet" href="https://fonts.googleapis.com/css2?family=Arimo:wght@400;700&family=Open+Sans:wght@400;600&display=swap">
<style>
  :root {
    --page-bg: #e4e4e6;
    --card-white: #ffffff;
    --card-black: #0b0b0b;
    --brand-red: #d8292f;
    --ink: #141414;
    --paper-white: #f4f4f4;
  }
  * { box-sizing: border-box; margin: 0; padding: 0; }
  html, body {
    width: 1200px; height: 960px; overflow: hidden;
    background: var(--page-bg);
  }
  body { position: relative; font-family: "Arimo", Arial, sans-serif; color: var(--ink); }

  .card {
    position: absolute; left: 300px; width: 600px; height: 343px;
    overflow: hidden;
    box-shadow: 0 6px 18px rgba(0,0,0,0.18);
  }
  .card--front { top: 110px; background: var(--card-white); }
  .card--back  { top: 507px; background: var(--card-black); }

  /* Front */
  .front__pointer { position: absolute; left: 0; top: 118px; }
  .contact-block { position: absolute; left: 62px; top: 110px; }
  .person__name { font-size: 26px; font-weight: 700; line-height: 1.1; }
  .person__title { font-size: 16px; margin-top: 2px; }
  .address { font-size: 16px; line-height: 1.3; margin-top: 12px; }
  .contact-list { list-style: none; margin-top: 10px; }
  .contact-list li {
    display: flex; align-items: center; gap: 10px;
    font-size: 16px; line-height: 1; height: 24px;
  }
  .contact-icon {
    width: 20px; height: 20px; border-radius: 3px;
    background: var(--brand-red); display: flex; align-items: center; justify-content: center;
  }

  .brand { position: absolute; right: 52px; top: 46px; text-align: right; }
  .brand__dot {
    width: 46px; height: 46px; border-radius: 50%;
    background: var(--brand-red); margin: 0 58px 16px auto;
  }
  .brand__name {
    font-family: "Arimo", Arial, sans-serif; font-weight: 700;
    color: var(--ink); line-height: 1.15; letter-spacing: 0.5px;
  }
  .brand__name span { display: block; }
  .brand__line--1 { font-size: 32px; }
  .brand__line--2 { font-size: 27px; }
  .brand__line--3 { font-size: 21px; }

  /* Back */
  .back__mark {
    position: absolute; left: 0; right: 0; top: 92px;
    display: flex; flex-direction: column; align-items: center; gap: 14px;
  }
  .back__dot { width: 62px; height: 62px; border-radius: 50%; background: var(--brand-red); }
  .back__name {
    font-family: "Arimo", Arial, sans-serif; font-weight: 700;
    font-size: 36px; letter-spacing: 2px; color: var(--brand-red);
  }
  .back__web {
    position: absolute; left: 0; right: 0; top: 254px; text-align: center;
    font-family: "Open Sans", Arial, sans-serif; font-weight: 600;
    font-size: 16px; letter-spacing: 1px; color: var(--paper-white);
  }
</style>
</head>
<body>

<section class="card card--front" aria-label="Business card front">
  <svg class="front__pointer" width="30" height="34" viewBox="0 0 30 34" aria-hidden="true">
    <polygon points="0,0 30,17 0,34" fill="var(--brand-red)"/>
  </svg>

  <div class="contact-block">
    <h1 class="person__name">Daniel Perera</h1>
    <p class="person__title">Director</p>
    <p class="address">18, Harbour View Road<br>Colombo 01000, Sri Lanka</p>
    <ul class="contact-list">
      <li>
        <span class="contact-icon">
          <svg width="11" height="15" viewBox="0 0 11 15" aria-hidden="true"><rect x="1" y="1" width="9" height="13" rx="1.5" fill="none" stroke="#fff" stroke-width="1.6"/><circle cx="5.5" cy="11.5" r="0.9" fill="#fff"/></svg>
        </span>+ 94 77 5120384
      </li>
      <li>
        <span class="contact-icon">
          <svg width="14" height="14" viewBox="0 0 24 24" aria-hidden="true"><path fill="#fff" d="M6.6 10.8a15 15 0 0 0 6.6 6.6l2.2-2.2c.3-.3.7-.4 1-.2 1.1.4 2.3.6 3.6.6.6 0 1 .4 1 1V20c0 .6-.4 1-1 1A17 17 0 0 1 3 4c0-.6.4-1 1-1h3.5c.6 0 1 .4 1 1 0 1.3.2 2.5.6 3.6.1.3 0 .7-.2 1z"/></svg>
        </span>+ 94 11 2450876
      </li>
      <li>
        <span class="contact-icon">
          <svg width="14" height="14" viewBox="0 0 14 14" aria-hidden="true"><rect x="3.5" y="1" width="7" height="4" fill="#fff"/><rect x="1" y="5" width="12" height="5" rx="1" fill="#fff"/><rect x="3.5" y="8.5" width="7" height="4.5" fill="#fff" stroke="var(--brand-red)" stroke-width="1"/></svg>
        </span>+ 94 11 2450877
      </li>
      <li>
        <span class="contact-icon">
          <svg width="14" height="11" viewBox="0 0 14 11" aria-hidden="true"><rect x="0.8" y="0.8" width="12.4" height="9.4" fill="none" stroke="#fff" stroke-width="1.4"/><polyline points="1,1 7,6 13,1" fill="none" stroke="#fff" stroke-width="1.4"/></svg>
        </span>info@crestmoorcolombo.com
      </li>
    </ul>
  </div>

  <div class="brand">
    <div class="brand__dot" aria-hidden="true"></div>
    <p class="brand__name">
      <span class="brand__line--1">CRESTMOOR</span>
      <span class="brand__line--2">CASINO</span>
      <span class="brand__line--3">COLOMBO</span>
    </p>
  </div>
</section>

<section class="card card--back" aria-label="Business card back">
  <div class="back__mark">
    <div class="back__dot" aria-hidden="true"></div>
    <p class="back__name">CRESTMOOR</p>
  </div>
  <p class="back__web">www.crestmoorcolombo.com</p>
</section>

</body>
</html>
```